Brightstone Roofing Business Card

This is my current business card. But I’d like to make some changes. Somewhere on the card I’d like to list some of the services we offer. Maybe on the back? But I’d still like to keep the red. White and black modern look.

-residential & commercial roofing
-Roof Repairs & Maintenance
-Storm Damage & Insurance Claims specialist
-Christmas Lights and permanent Christmas lights
Fencing. Windows. Gutters. Siding. Sheetrock, painting.

```html
<!DOCTYPE html>
<html lang="en">
<head>
<meta charset="utf-8">
<title>Brightstone Roofing Business Card</title>
<link rel="stylesheet" href="https://fonts.googleapis.com/css2?family=Audiowide&family=Open+Sans:wght@400;600;700&display=swap">
<style>
  :root {
    --red: #d92d27;
    --black: #050607;
    --white: #ffffff;
    --ink: #111111;
    --backdrop: #3b3b3d;
  }
  * { box-sizing: border-box; margin: 0; padding: 0; }
  html, body { width: 1200px; height: 1059px; overflow: hidden; }
  body {
    background: var(--backdrop);
    font-family: "Open Sans", Arial, sans-serif;
    position: relative;
  }
  .card {
    position: absolute;
    left: 255px;
    width: 690px;
    height: 392px;
    border-radius: 20px;
    overflow: hidden;
    box-shadow: 0 10px 24px rgba(0,0,0,0.45);
  }
  .card--front { top: 100px; background: var(--white); }
  .card--back { top: 537px; background: var(--black); }

  .brand {
    position: absolute;
    left: 0; right: 0;
    text-align: center;
  }
  .brand__dot {
    display: block;
    margin: 0 auto;
    border-radius: 50%;
    background: var(--red);
  }
  .card--front .brand { top: 45px; }
  .card--front .brand__dot { width: 106px; height: 106px; }
  .card--back .brand { top: 68px; }
  .card--back .brand__dot { width: 128px; height: 128px; }

  .brand__name {
    color: var(--red);
    font-weight: 700;
    text-transform: uppercase;
    line-height: 1.05;
    letter-spacing: 0.5px;
  }
  .card--front .brand__name { font-size: 25px; margin-top: 22px; }
  .card--back .brand__name { font-size: 29px; margin-top: 20px; }
  .brand__name span { display: block; font-size: 0.72em; }

  .person {
    position: absolute;
    right: 371px;
    top: 275px;
    text-align: right;
  }
  .person__name {
    font-family: "Audiowide", sans-serif;
    font-size: 24px;
    line-height: 1;
    color: var(--ink);
    text-transform: uppercase;
  }
  .person__name em { font-style: normal; color: var(--red); }
  .person__role {
    margin-top: 8px;
    font-size: 15px;
    color: var(--red);
    letter-spacing: 0.5px;
  }
  .divider {
    position: absolute;
    left: 342px;
    top: 270px;
    width: 1.5px;
    height: 69px;
    background: var(--ink);
  }
  .contact {
    position: absolute;
    left: 367px;
    top: 266px;
    list-style: none;
  }
  .contact li {
    display: flex;
    align-items: center;
    height: 26px;
    font-size: 16px;
    color: var(--ink);
  }
  .contact li.phone { letter-spacing: 2.2px; }
  .contact svg { width: 13px; height: 13px; margin-right: 9px; flex: none; }

  .services {
    position: absolute;
    left: 0; right: 0;
    top: 305px;
    list-style: none;
    display: flex;
    flex-wrap: wrap;
    justify-content: center;
    column-gap: 8px;
    row-gap: 6px;
    padding: 0 26px;
    color: var(--white);
    font-size: 15.5px;
  }
  .services li { white-space: nowrap; }
  .services li::before {
    content: "";
    display: inline-block;
    width: 7px; height: 7px;
    border-radius: 50%;
    background: var(--red);
    margin-right: 7px;
    vertical-align: middle;
    position: relative;
    top: -1px;
  }
  .band {
    position: absolute;
    left: 0; bottom: 0;
    width: 690px; height: 15px;
  }
</style>
</head>
<body>

<section class="card card--front" aria-label="Card front">
  <div class="brand">
    <span class="brand__dot"></span>
    <p class="brand__name">Brightstone<span>Roofing Co.</span></p>
  </div>

  <div class="person">
    <p class="person__name"><em>Dale</em> Mercer</p>
    <p class="person__role">OWNER</p>
  </div>
  <div class="divider"></div>
  <ul class="contact">
    <li class="phone">
      <svg viewBox="0 0 24 24"><path fill="#d92d27" d="M6.6 10.8a15.1 15.1 0 0 0 6.6 6.6l2.2-2.2c.3-.3.7-.4 1-.2 1.1.4 2.3.6 3.6.6.6 0 1 .4 1 1V20c0 .6-.4 1-1 1A17 17 0 0 1 3 4c0-.6.4-1 1-1h3.5c.6 0 1 .4 1 1 0 1.3.2 2.5.6 3.6.1.3 0 .7-.2 1z"/></svg>
      214-555-0186
    </li>
    <li>
      <svg viewBox="0 0 24 24"><rect x="2" y="5" width="20" height="14" rx="2" fill="#d92d27"/><path d="M3 6l9 7 9-7" fill="none" stroke="#fff" stroke-width="1.8"/></svg>
      dale@brightstoneroofing.co
    </li>
    <li>
      <svg viewBox="0 0 24 24" fill="none" stroke="#d92d27" stroke-width="1.8"><circle cx="12" cy="12" r="9.5"/><ellipse cx="12" cy="12" rx="4" ry="9.5"/><path d="M2.5 12h19M4 7h16M4 17h16"/></svg>
      www.brightstoneroofing.co
    </li>
  </ul>

  <svg class="band" viewBox="0 0 690 15" preserveAspectRatio="none">
    <polygon points="0,0 351,0 336,15 0,15" fill="var(--red)"/>
    <polygon points="358,0 690,0 690,15 343,15" fill="var(--black)"/>
  </svg>
</section>

<section class="card card--back" aria-label="Card back">
  <div class="brand">
    <span class="brand__dot"></span>
    <p class="brand__name">Brightstone<span>Roofing Co.</span></p>
  </div>

  <ul class="services">
    <li>Residential &amp; commercial roofing</li>
    <li>Storm Damage &amp; Insurance Claims specialist</li>
    <li>Roof Repairs &amp; Maintenance</li>
    <li>Christmas Lights and permanent Christmas lights</li>
  </ul>

  <svg class="band" viewBox="0 0 690 15" preserveAspectRatio="none">
    <polygon points="0,0 351,0 336,15 0,15" fill="var(--red)"/>
    <polygon points="358,0 690,0 690,15 343,15" fill="var(--white)"/>
  </svg>
</section>

</body>
</html>
```